Harbor Peak Ventures Stationary
Harbor Peak Ventures
Project: Harbor Peak Ventures Stationary
Harbor Peak Ventures Stationary - Financial Services
Creative Brief
Corporate
Mark Torvalen
Managing Partner
214 Willow Fen Lane Fayetteville, NY 13412
mtorvalen@harborpeakventures.example
214 Willow Fen Lane
www.harborpeakventures.example

```html
<!DOCTYPE html>
<html lang="en">
<head>
<meta charset="utf-8">
<title>Harbor Peak Ventures – Business Card</title>
<link rel="stylesheet" href="https://fonts.googleapis.com/css2?family=Tinos&display=swap">
<style>
  :root {
    --page-bg: #e9eaec;
    --card-bg: #ffffff;
    --brand-blue: #0a4d7a;
    --title-ink: #2b2b2b;
    --detail-ink: #5a5a5a;
  }
  * { margin: 0; padding: 0; box-sizing: border-box; }
  html, body {
    width: 1200px;
    height: 751px;
    overflow: hidden;
    background: var(--page-bg);
  }
  .business-card {
    position: absolute;
    left: 30px;
    top: 50px;
    width: 1140px;
    height: 652px;
    background: var(--card-bg);
    font-family: "Tinos", "Times New Roman", serif;
  }
  .brand-name {
    position: absolute;
    left: 0;
    right: 0;
    top: 92px;
    text-align: center;
    font-size: 84px;
    line-height: 1;
    font-weight: 400;
    color: var(--brand-blue);
    white-space: nowrap;
  }
  .holder {
    position: absolute;
    left: 0;
    right: 0;
    top: 318px;
    text-align: center;
  }
  .holder-name {
    font-size: 57px;
    line-height: 1.1;
    font-weight: 400;
    color: var(--brand-blue);
  }
  .holder-title {
    margin-top: 6px;
    font-size: 30px;
    line-height: 1.1;
    color: var(--title-ink);
  }
  .contact-lines {
    position: absolute;
    left: 74px;
    top: 466px;
    list-style: none;
    font-size: 28px;
    line-height: 44px;
    color: var(--detail-ink);
  }
  .postal-address {
    position: absolute;
    right: 63px;
    top: 484px;
    text-align: right;
    font-style: normal;
    font-size: 28px;
    line-height: 37px;
    color: var(--detail-ink);
  }
</style>
</head>
<body>
  <article class="business-card">
    <h1 class="brand-name">Harbor Peak Ventures</h1>

    <header class="holder">
      <h2 class="holder-name">Mark Torvalen</h2>
      <p class="holder-title">Managing Partner</p>
    </header>

    <ul class="contact-lines">
      <li class="contact-phone">+1 315-555-0142</li>
      <li class="contact-email">mtorvalen@harborpeakventures.example</li>
      <li class="contact-web">www.harborpeakventures.example</li>
    </ul>

    <address class="postal-address">
      214 Willow Fen Lane<br>
      Fayetteville, NY 13412
    </address>
  </article>
</body>
</html>
```